Tarn’s Beauty. Coffee Scrub Skincare

Graphic design for my Coffee Scrub skin care business. Tarn’s Beauty. To go on the packaging. Fun with pastel colours, but still clean and professional. See attached photos on similar businesses packaging. I like the “Bree & Ula” font (see attached photo).

Things to write on the packaging: Tarn’s Beauty. Recycled Coffee scrub. Coconut and Chocolate. Recycled packaging. Vegan. Not tested on animal. Recycled coffee. Pink Australian clay. 150g 5.29 oz. Made in Australia.

```html
<!DOCTYPE html>
<html lang="en">
<head>
<meta charset="utf-8">
<title>Tarn’s Beauty – Recycled Coffee Scrub Labels</title>
<link rel="stylesheet" href="https://fonts.googleapis.com/css2?family=Big+Shoulders+Display:wght@600&family=Didact+Gothic&family=Noto+Serif&display=swap">
<style>
  :root {
    --canvas: #ffffff;
    --pink: #f4bfd3;
    --pink-soft: #f7cddc;
    --teal: #9fd9dc;
    --teal-deep: #73c8ca;
    --teal-pale: #d9eff1;
    --sky: #bfe0f3;
    --sky-pale: #d6ebf4;
    --ink: #111111;
    --display: "Big Shoulders Display", "Arial Narrow", sans-serif;
    --sans: "Didact Gothic", Arial, sans-serif;
    --serif: "Noto Serif", Georgia, serif;
  }
  * { box-sizing: border-box; margin: 0; padding: 0; }
  html, body { width: 1200px; height: 998px; overflow: hidden; background: var(--canvas); }
  .canvas { position: relative; width: 1200px; height: 998px; }

  .label {
    position: absolute;
    width: 600px; height: 812px;
    background: var(--teal);
    overflow: hidden;
    box-shadow: 2px 3px 4px rgba(0,0,0,0.35);
    color: var(--ink);
    font-family: var(--sans);
    transform-origin: 0 0;
  }
  .label--large { left: 96px; top: 93px; }
  .label--small { left: 757px; top: 400px; transform: scale(0.663); }

  .label__icing { position: absolute; left: 0; top: 0; width: 600px; height: 300px; }
  .label__stitch { position: absolute; left: 0; top: 57px; width: 600px; border-top: 2px dashed rgba(255,255,255,0.85); }

  .label__blob { position: absolute; }
  .label__blob--sky { left: 346px; top: 543px; width: 300px; height: 300px; background: var(--sky); border-radius: 50% 38% 0 46%; }
  .label__blob--deep { left: -20px; top: 612px; width: 250px; height: 230px; background: var(--teal-deep); border-radius: 42% 58% 0 0; }

  .art { position: absolute; }
  .art--coconut {
    left: 285px; top: 520px; width: 285px; height: 255px;
    background: linear-gradient(160deg, var(--sky-pale), #aed6e2);
    border-radius: 58% 42% 46% 54% / 52% 44% 56% 48%;
  }
  .art--cacao {
    left: 32px; top: 640px; width: 190px; height: 138px;
    background: linear-gradient(150deg, var(--teal-pale), #bfe3e6);
    border-radius: 54% 46% 40% 60% / 50% 56% 44% 50%;
  }

  .label__kicker { position: absolute; left: 0; width: 100%; top: 216px; padding-left: 6px; text-align: center; font-size: 21px; }
  .label__brand {
    position: absolute; left: 0; width: 100%; top: 316px;
    text-align: center; font-family: var(--display); font-weight: 600;
    font-size: 86px; line-height: 1; letter-spacing: 1px; text-transform: uppercase;
  }

  .flavour { position: absolute; top: 425px; height: 59px; border: 1.5px dashed var(--ink); font-size: 34px; line-height: 56px; text-align: center; }
  .flavour--coconut { left: 64px; width: 184px; }
  .flavour--chocolate { left: 323px; width: 213px; }
  .flavour__and { position: absolute; left: 264px; top: 447px; font-size: 21px; }

  .claims { position: absolute; left: 207px; top: 492px; list-style: none; font-family: var(--serif); font-size: 17.5px; line-height: 20px; }
  .claims li { display: flex; align-items: center; gap: 3px; }
  .claims svg { width: 8px; height: 11px; }

  .features { position: absolute; left: 64px; top: 567px; list-style: none; font-size: 26px; line-height: 27px; }
  .features li { display: flex; align-items: center; gap: 3px; }
  .features svg { width: 12px; height: 16px; }

  .label__origin { position: absolute; left: 190px; width: 220px; top: 711px; text-align: center; font-size: 20px; }
  .label__weight { position: absolute; left: 190px; width: 220px; top: 748px; text-align: center; font-family: Arial, sans-serif; font-size: 22px; }
</style>
</head>
<body>
<main class="canvas">

  <article class="label label--large">
    <svg class="label__icing" viewBox="0 0 600 300" role="img" aria-label="Pink icing band with a pattern of white palm leaves and dots">
      <defs>
        <linearGradient id="icing-large" x1="0" y1="0" x2="0" y2="1">
          <stop offset="0" stop-color="var(--pink-soft)"/>
          <stop offset="1" stop-color="var(--pink)"/>
        </linearGradient>
      </defs>
      <path fill="url(#icing-large)" d="M0 0H600V215Q596 262 578 250Q560 235 548 255Q535 290 515 265Q500 240 480 258Q462 300 440 268Q425 240 405 255Q388 275 370 262Q352 240 332 262Q312 300 292 270Q278 245 255 255Q232 300 210 262Q198 240 178 250Q158 275 140 258Q122 235 100 252Q80 300 58 262Q45 230 25 238Q8 245 0 228Z"/>
    </svg>
    <div class="label__blob label__blob--sky"></div>
    <div class="label__blob label__blob--deep"></div>
    <div class="art art--coconut" role="img" aria-label="Line illustration of a halved coconut with palm leaves"></div>
    <div class="art art--cacao" role="img" aria-label="Line illustration of a cacao pod with beans"></div>

    <p class="label__kicker">RECYCLED COFFEE SCRUB</p>
    <h1 class="label__brand">Tarn’s Beauty</h1>
    <span class="flavour flavour--coconut">COCONUT</span>
    <span class="flavour__and">AND</span>
    <span class="flavour flavour--chocolate">CHOCOLATE</span>
    <ul class="claims">
      <li><svg viewBox="0 0 8 11"><path d="M4 0C6 4 8 6 8 7.5A4 4 0 0 1 0 7.5C0 6 2 4 4 0Z"/></svg>Recycled packaging</li>
      <li><svg viewBox="0 0 8 11"><path d="M4 0C6 4 8 6 8 7.5A4 4 0 0 1 0 7.5C0 6 2 4 4 0Z"/></svg>Not tested on animal</li>
      <li><svg viewBox="0 0 8 11"><path d="M4 0C6 4 8 6 8 7.5A4 4 0 0 1 0 7.5C0 6 2 4 4 0Z"/></svg>Recycled coffee</li>
    </ul>
    <ul class="features">
      <li><svg viewBox="0 0 12 16"><path d="M0 0L12 8L0 16Z"/></svg>PINK AUSTRALIAN CLAY</li>
      <li><svg viewBox="0 0 12 16"><path d="M0 0L12 8L0 16Z"/></svg>VEGAN</li>
    </ul>
    <p class="label__origin">MADE IN AUSTRALIA</p>
    <p class="label__weight">150g 5.29 oz</p>
  </article>

  <article class="label label--small">
    <svg class="label__icing" viewBox="0 0 600 300" role="img" aria-label="Pink icing band with a pattern of white palm leaves and dots">
      <defs>
        <linearGradient id="icing-small" x1="0" y1="0" x2="0" y2="1">
          <stop offset="0" stop-color="var(--pink-soft)"/>
          <stop offset="1" stop-color="var(--pink)"/>
        </linearGradient>
      </defs>
      <path fill="url(#icing-small)" d="M0 0H600V215Q596 262 578 250Q560 235 548 255Q535 290 515 265Q500 240 480 258Q462 300 440 268Q425 240 405 255Q388 275 370 262Q352 240 332 262Q312 300 292 270Q278 245 255 255Q232 300 210 262Q198 240 178 250Q158 275 140 258Q122 235 100 252Q80 300 58 262Q45 230 25 238Q8 245 0 228Z"/>
    </svg>
    <div class="label__stitch"></div>
    <div class="label__blob label__blob--sky"></div>
    <div class="label__blob label__blob--deep"></div>
    <div class="art art--coconut" role="img" aria-label="Line illustration of a halved coconut with palm leaves"></div>
    <div class="art art--cacao" role="img" aria-label="Line illustration of a cacao pod with beans"></div>

    <p class="label__kicker">RECYCLED COFFEE SCRUB</p>
    <h2 class="label__brand">Tarn’s Beauty</h2>
    <span class="flavour flavour--coconut">COCONUT</span>
    <span class="flavour__and">AND</span>
    <span class="flavour flavour--chocolate">CHOCOLATE</span>
    <ul class="claims">
      <li><svg viewBox="0 0 8 11"><path d="M4 0C6 4 8 6 8 7.5A4 4 0 0 1 0 7.5C0 6 2 4 4 0Z"/></svg>Recycled packaging</li>
      <li><svg viewBox="0 0 8 11"><path d="M4 0C6 4 8 6 8 7.5A4 4 0 0 1 0 7.5C0 6 2 4 4 0Z"/></svg>Not tested on animal</li>
      <li><svg viewBox="0 0 8 11"><path d="M4 0C6 4 8 6 8 7.5A4 4 0 0 1 0 7.5C0 6 2 4 4 0Z"/></svg>Recycled coffee</li>
    </ul>
    <ul class="features">
      <li><svg viewBox="0 0 12 16"><path d="M0 0L12 8L0 16Z"/></svg>PINK AUSTRALIAN CLAY</li>
      <li><svg viewBox="0 0 12 16"><path d="M0 0L12 8L0 16Z"/></svg>VEGAN</li>
    </ul>
    <p class="label__origin">MADE IN AUSTRALIA</p>
    <p class="label__weight">150g 5.29 oz</p>
  </article>

</main>
</body>
</html>
```